BUSINESS CARD needed for TRAVEL BUSINESS

-Background-

Wandorvist Crew (WC) is a newly found company in Asia that trains and develops people with various demographics to become a FREQUENT TRAVELER & an ENTREPRENEUR combined. Basically, the core product that the company markets teaches people how to TRAVEL leisurely and yet EARN MONEY at the same time. Our main quote will be LIVING LIFE BY LIVING.

- The Job -

We will be constantly going out to different events, whether opening promotional booths in roadshows or at colleges or going for networking events. Thus we need a BUSINESS CARD design that portrays our POSITIONING & BRANDING

- Positioning -

TRAVEL LEISURELY & EARN at the SAME TIME

- Objective -

Serve as a BTL marketing & networking tool

- Target Audience -

Male & Females aged 19 - 35 who LOVES to TRAVEL & have strong aspirations to make it big and attaining financial freedom. The audience are enthusiastic and when they see an opportunity, they will seize it on the very spot. They are well connected and have a wide social network.

- Single Minded Proposition -

WC is My Dream Life

Target Market(s)

REFER TO CREATIVE BRIEF

Industry/Entity Type

Marketing

Requirements
Must have
• 1) The business card must portray a branding thats related to TRAVEL.

Boarding pass design was what we came up with but express your creativity and surprise me with better ideas. :)
Nice to have
• This is an idea that we have and we would most likely like to use however I do not want to restrict your creativity so i am putting in NICE TO HAVE instead.

Our idea design -> To have the namecard in the format of a BOARDING PASS lookalike

(You may refer to these weblink for inspiration -> https://www.pictofind.example/search?hl=en&q=boarding+pass&bav=on.2,or.r_gc.r_pw.r_cp.r_qf.,cf.osb&biw=1366&bih=667&um=1&ie=UTF-8&tbm=isch&source=og&sa=N&tab=wi&ei=l-f9T4KqC4fWrQfx8eC-Bg

or simply PICTOFIND BOARDING PASS IMAGES

```html
<!DOCTYPE html>
<html lang="en">
<head>
<meta charset="utf-8">
<title>Wandorvist Crew – Boarding Pass Business Card</title>
<link rel="stylesheet" href="https://fonts.googleapis.com/css2?family=Michroma&display=swap">
<style>
  :root{
    --blue-deep:#0a6fb8;
    --blue:#1a9ad9;
    --blue-light:#4fc0ef;
    --blue-pale:#8fd8f6;
    --band:#231f20;
    --paper:#ffffff;
    --ink:#1a1a1a;
    --frame:#4a4a4a;
    --rule:#d8d8d8;
  }
  *{box-sizing:border-box;margin:0;padding:0}
  html,body{width:1040px;height:1200px;overflow:hidden;background:#fff}
  body{position:relative;font-family:"Michroma",sans-serif;color:var(--paper)}

  .pass{position:absolute;left:6px;width:1028px;height:590px;border:2px solid var(--frame);overflow:hidden;background:var(--paper)}
  .pass--one{top:4px}
  .pass--two{top:604px}

  .pass__bg{position:absolute;inset:0}
  .artwork{position:absolute}

  .passenger-label{position:absolute;left:16px;top:62px;font-size:15px;letter-spacing:1px}
  .passenger-name{position:absolute;left:14px;top:102px;font-size:48px;line-height:1;letter-spacing:1px;white-space:nowrap}

  .brand{position:absolute;display:flex;align-items:center;gap:12px;white-space:nowrap}
  .brand__mark{width:34px;height:34px;border-radius:50%}
  .brand__name{font-size:20px;letter-spacing:2px}
  .company{position:absolute;text-align:center;width:490px;white-space:nowrap}
  .company__name{font-size:36px;font-variant:small-caps;letter-spacing:0;line-height:1}
  .company__tag{font-size:13px;letter-spacing:1px;margin-top:8px}
  .company__position{font-size:18px;letter-spacing:2px;margin-top:4px}

  .details{position:absolute;left:0;top:202px;width:864px;height:184px;background:var(--band);display:flex}
  .details__col{position:relative;padding-top:26px;text-align:center;border-right:2px dashed var(--rule);white-space:nowrap}
  .details__col:last-child{border-right:none}
  .details__col:nth-child(1){width:205px;text-align:left;padding-left:14px}
  .details__col:nth-child(2){width:181px}
  .details__col:nth-child(3){width:184px}
  .details__col:nth-child(4){width:294px}
  .details__label{font-size:13px;letter-spacing:2px;line-height:1.3}
  .details__value{font-size:16px;line-height:1.65}
  .details__col:nth-child(1) .details__value{margin-top:24px}
  .details__col:nth-child(2) .details__value,
  .details__col:nth-child(3) .details__value{margin-top:54px}
  .details__col:nth-child(4) .details__value{margin-top:34px}

  .flight{position:absolute;text-align:center;width:250px;white-space:nowrap}
  .flight__date{font-size:17px;letter-spacing:1px;padding-bottom:10px;border-bottom:2px dashed currentColor}
  .flight__class{font-size:17px;letter-spacing:1px;margin-top:12px}
  .flight-time{position:absolute;width:124px;height:60px;border-radius:22px;background:var(--band);color:var(--paper);display:flex;align-items:center;justify-content:center;font-size:17px;border:2px solid var(--paper);white-space:nowrap}

  .ref{position:absolute;font-size:7px;line-height:1.6;color:var(--ink);width:124px;white-space:nowrap;letter-spacing:-0.2px}
  .ref__row{display:flex;justify-content:space-between}
  .ref--light{color:var(--paper)}

  .stub{position:absolute;top:0;left:864px;width:162px;height:586px;background:var(--paper);color:var(--ink)}
  .pass--one .stub{border-left:2px dashed var(--paper)}
  .pass--two .stub{border-left:2px dashed var(--blue)}
  .stub .ref{left:20px;top:80px}
  .stub__name,.stub__phone{position:absolute;writing-mode:vertical-rl;transform:rotate(180deg);white-space:nowrap;line-height:1}
  .stub__name{left:22px;bottom:12px;font-size:54px;letter-spacing:2px}
  .stub__phone{left:108px;bottom:64px;font-size:27px;letter-spacing:2px}

  .pass--two .brand,.pass--two .company{color:var(--ink)}
  .pass--two .flight{color:var(--ink)}
</style>
</head>
<body>

<section class="pass pass--one">
  <svg class="pass__bg" width="1028" height="590" viewBox="0 0 1028 590" aria-hidden="true">
    <defs>
      <linearGradient id="skyTop" x1="0" x2="1" y1="0" y2="0">
        <stop offset="0" stop-color="#0a7ac4"/>
        <stop offset="0.55" stop-color="#2aaae6"/>
        <stop offset="1" stop-color="#1692d4"/>
      </linearGradient>
      <linearGradient id="skyBottom" x1="0" x2="1" y1="0" y2="1">
        <stop offset="0" stop-color="#0e86cf"/>
        <stop offset="0.5" stop-color="#3ab6ec"/>
        <stop offset="1" stop-color="#1690d3"/>
      </linearGradient>
    </defs>
    <rect x="0" y="0" width="866" height="202" fill="url(#skyTop)"/>
    <rect x="0" y="386" width="866" height="204" fill="url(#skyBottom)"/>
  </svg>

  <div class="artwork" role="img" aria-label="Jet airliner flying past a pale world map" style="left:0;top:386px;width:500px;height:204px;background:linear-gradient(100deg,#0b5ea3 0%,#5cc3ef 45%,rgba(143,216,246,.35) 100%)"></div>

  <p class="passenger-label">PASSENGER</p>
  <h1 class="passenger-name">REN AOKI</h1>

  <div class="brand" style="left:455px;top:28px">
    <span class="brand__mark" style="background:var(--blue-pale)"></span>
    <span class="brand__name">ORIENT ONWARD</span>
  </div>
  <div class="company" style="left:370px;top:100px">
    <p class="company__name">Wandorvist Crew</p>
    <p class="company__tag">BOARDING PASS</p>
    <p class="company__position">COMPANY POSITION</p>
  </div>

  <div class="details">
    <div class="details__col"><p class="details__label">DESTINATION</p><p class="details__value">4567 MAIN ST.<br>CITY, ST<br>&nbsp;&nbsp;45678</p></div>
    <div class="details__col"><p class="details__label">PHONE NO.</p><p class="details__value">555-555-555</p></div>
    <div class="details__col"><p class="details__label">FAX NO.</p><p class="details__value">555-555-555</p></div>
    <div class="details__col"><p class="details__label">E-MAIL AND ANY<br>ADDITIONAL INFO.</p><p class="details__value">NAME@WEB.EXAMPLE</p></div>
  </div>

  <div class="ref ref--light" style="left:722px;top:396px">
    <p>1 234 56789101 112 13 4</p>
    <p class="ref__row"><span>AB00015</span><span>CD61E31</span></p>
  </div>

  <div class="flight" style="left:494px;top:478px">
    <p class="flight__date">JULY 13, 2012</p>
    <p class="flight__class">FIRST CLASS</p>
  </div>
  <div class="flight-time" style="left:728px;top:506px">4:00 PM</div>

  <aside class="stub">
    <div class="ref">
      <p>1 234 56789101 112 13 4</p>
      <p class="ref__row"><span>AB00015</span><span>CD61E31</span></p>
    </div>
    <p class="stub__name">REN AOKI</p>
    <p class="stub__phone">555-555-555</p>
  </aside>
</section>

<section class="pass pass--two">
  <svg class="pass__bg" width="1028" height="590" viewBox="0 0 1028 590" aria-hidden="true">
    <defs>
      <linearGradient id="panelBlue" x1="0" x2="1" y1="0" y2="1">
        <stop offset="0" stop-color="#1b9ee0"/>
        <stop offset="1" stop-color="#4cc0ef"/>
      </linearGradient>
    </defs>
    <polygon points="0,0 322,0 382,202 0,202" fill="url(#panelBlue)"/>
    <rect x="0" y="0" width="154" height="202" fill="#1384cc"/>
    <polygon points="0,386 458,386 530,590 0,590" fill="url(#panelBlue)"/>
    <rect x="0" y="386" width="154" height="204" fill="#1384cc"/>
  </svg>

  <div class="artwork" role="img" aria-label="Pale world map silhouette" style="left:186px;top:400px;width:264px;height:130px;background:radial-gradient(ellipse at center,rgba(190,232,250,.7),rgba(190,232,250,0) 70%)"></div>
  <div class="artwork" role="img" aria-label="Jumbo jet airliner in flight" style="left:478px;top:400px;width:236px;height:110px;background:radial-gradient(ellipse at center,#b9d4e6 0%,#e4eef5 55%,rgba(255,255,255,0) 75%)"></div>

  <p class="passenger-label">PASSENGER</p>
  <h1 class="passenger-name">REN AOKI</h1>

  <div class="brand" style="left:455px;top:26px">
    <span class="brand__mark" style="background:var(--blue)"></span>
    <span class="brand__name">ORIENT ONWARD</span>
  </div>
  <div class="company" style="left:370px;top:98px">
    <p class="company__name">Wandorvist Crew</p>
    <p class="company__tag">BOARDING PASS</p>
    <p class="company__position">COMPANY POSITION</p>
  </div>

  <div class="details">
    <div class="details__col"><p class="details__label">DESTINATION</p><p class="details__value">4567 MAIN ST.<br>CITY, ST<br>&nbsp;&nbsp;45678</p></div>
    <div class="details__col"><p class="details__label">PHONE NO.</p><p class="details__value">555-555-555</p></div>
    <div class="details__col"><p class="details__label">FAX NO.</p><p class="details__value">555-555-555</p></div>
    <div class="details__col"><p class="details__label">E-MAIL AND ANY<br>ADDITIONAL INFO.</p><p class="details__value">NAME@WEB.EXAMPLE</p></div>
  </div>

  <div class="ref" style="left:722px;top:400px">
    <p>1 234 56789101 112 13 4</p>
    <p class="ref__row"><span>AB00015</span><span>CD61E31</span></p>
  </div>

  <div class="flight" style="left:186px;top:452px">
    <p class="flight__date">JULY 13, 2012</p>
    <p class="flight__class">FIRST CLASS</p>
  </div>
  <div class="flight-time" style="left:18px;top:488px">4:00 PM</div>

  <aside class="stub">
    <div class="ref">
      <p>1 234 56789101 112 13 4</p>
      <p class="ref__row"><span>AB00015</span><span>CD61E31</span></p>
    </div>
    <p class="stub__name">REN AOKI</p>
    <p class="stub__phone">555-555-555</p>
  </aside>
</section>

</body>
</html>
```